New Business Card Design Project

I need a design for business cards, i am an electrical business called "Tandor Electrical and Communications" i need the cards to be double sided with the company logo on the back (attached) the front needs to say my company name, web site, email address, telephone number, and ABN number and electrical license number. I am open to different arrangements of the information but would like the background to be incorporating something electrical or something that looks smart. open to all additional ideas also.

The company colours are orange and grey see logo attached.

Business Name: Tandor Electrical and Communications
Website: tandorelectricalandcomms.example.au
Email: brent@tandorelectricalandcomms.example.au
Telephone(mobile): 0481203967
ABN: 71829034618
Lic No: 830472F

Target Market(s)

Business entities, Project Managers, Accounts, Clients

Industry/Entity Type

Electrician

Contact Information for Business Card

I need a design for business cards, i am an electrical business called "Tandor Electrical and Communications" i need the cards to be double sided with the company logo on the back (attached) the front needs to say my company name

Font styles to use
Serif
Sans Serif

Colors
f37122
5c5c5c

Requirements
Must have
• Must have the Logo on the back open to different ways of it being on the back but had in mind to keep it central but again open to other options
Nice to have
• A real modern cool background that is eye catching yet contemporary
Should not have
• No backgrounds of a light bulb or plug or anything like that

```html
<!DOCTYPE html>
<html lang="en">
<head>
<meta charset="utf-8">
<title>Tandor Electrical and Communications – Business Cards</title>
<link href="https://fonts.googleapis.com/css2?family=Open+Sans:wght@400;600&family=Exo+2:wght@500&display=swap" rel="stylesheet">
<style>
  :root {
    --backdrop: #e9e7e3;
    --card-white: #fbfbfb;
    --card-grey: #5c5c5c;
    --card-grey-dark: #4a4a4a;
    --line-grey: #7a7a7a;
    --accent: #f2c11c;
    --ink-grey: #6a6a6a;
    --ink-light: #f4f4f4;
  }
  * { box-sizing: border-box; margin: 0; padding: 0; }
  html, body { width: 1200px; height: 780px; overflow: hidden; }
  body {
    background: var(--backdrop);
    font-family: "Open Sans", Arial, sans-serif;
    position: relative;
  }
  .card {
    position: absolute;
    width: 540px;
    height: 330px;
    border-radius: 4px;
    overflow: hidden;
    box-shadow: 0 3px 0 #d0d0d0, 0 6px 0 #bdbdbd, 0 12px 24px rgba(0,0,0,.25);
  }
  .card--front { left: 40px; top: 100px; background: var(--card-white); }
  .card--back {
    left: 620px; top: 350px;
    background: radial-gradient(ellipse at 50% 45%, #6e6e6e 0%, var(--card-grey) 55%, var(--card-grey-dark) 100%);
  }
  .card__swoosh { position: absolute; inset: 0; }

  .wordmark { position: absolute; font-family: "Exo 2", sans-serif; font-weight: 500; line-height: 1; }
  .wordmark__name { display: block; letter-spacing: 3px; }
  .wordmark__tag { display: block; letter-spacing: 1px; text-transform: uppercase; }
  .card--front .wordmark { left: 30px; top: 140px; color: var(--ink-grey); }
  .card--front .wordmark__name { font-size: 44px; }
  .card--front .wordmark__tag { font-size: 10.5px; margin-top: 8px; color: var(--accent); }
  .card--back .wordmark { left: 0; right: 0; top: 110px; text-align: center; color: var(--ink-light); }
  .card--back .wordmark__name { font-size: 70px; }
  .card--back .wordmark__tag { font-size: 14px; margin-top: 12px; color: var(--accent); }

  .employee { position: absolute; left: 110px; top: 20px; width: 180px; text-align: right; }
  .employee__name { font-size: 20px; color: var(--ink-grey); letter-spacing: .5px; line-height: 1.3; }
  .employee__role { font-size: 13px; color: var(--accent); line-height: 1.3; }

  .contact {
    position: absolute; right: 16px; top: 34px;
    color: var(--ink-light); font-size: 10.5px; text-align: right; line-height: 2;
  }
  .contact__label { color: var(--accent); font-weight: 600; }
  .contact__line { display: flex; justify-content: flex-end; align-items: center; gap: 6px; }
  .contact__gap { height: 104px; }
  .icon {
    width: 13px; height: 13px; background: var(--accent); border-radius: 2px;
    display: inline-flex; align-items: center; justify-content: center; flex: none;
  }
  .icon svg { width: 9px; height: 9px; }
</style>
</head>
<body>

<section class="card card--front" aria-label="Business card front">
  <svg class="card__swoosh" viewBox="0 0 540 330" preserveAspectRatio="none" aria-hidden="true">
    <path d="M210 330 C270 270 200 120 380 0 L540 0 L540 330 Z" fill="var(--card-grey)"/>
    <path d="M194 330 C254 270 184 120 364 0" fill="none" stroke="var(--line-grey)" stroke-width="6"/>
    <path d="M150 330 C215 280 200 200 240 140 C220 210 245 280 200 330 Z" fill="var(--accent)"/>
  </svg>

  <div class="wordmark">
    <span class="wordmark__name">TANDOR</span>
    <span class="wordmark__tag">Electrical &amp; Communications</span>
  </div>

  <div class="employee">
    <p class="employee__name">Employee Name</p>
    <p class="employee__role">Principal</p>
  </div>

  <div class="contact">
    <p><span class="contact__label">Lic No:</span> 830472F</p>
    <p><span class="contact__label">ABN:</span> 71829034618</p>
    <p class="contact__line">0481203967
      <span class="icon"><svg viewBox="0 0 10 10"><path d="M2 1h2l1 2-1 1c.6 1.2 1.4 2 2.6 2.6l1-1 2 1v2c0 .5-.4.8-.9.8C4.3 9 1 5.7 1 1.9 1 1.4 1.4 1 2 1z" fill="#5c5c5c"/></svg></span></p>
    <div class="contact__gap"></div>
    <p class="contact__line">brent@tandorelectricalandcomms.example.au
      <span class="icon"><svg viewBox="0 0 10 10"><rect x="1" y="2.5" width="8" height="5" fill="none" stroke="#5c5c5c"/><path d="M1 2.5l4 3 4-3" fill="none" stroke="#5c5c5c"/></svg></span></p>
    <p class="contact__line">tandorelectricalandcomms.example.au
      <span class="icon"><svg viewBox="0 0 10 10"><circle cx="5" cy="5" r="4" fill="none" stroke="#5c5c5c"/><path d="M1 5h8M5 1c-2 2.5-2 5.5 0 8M5 1c2 2.5 2 5.5 0 8" fill="none" stroke="#5c5c5c" stroke-width=".8"/></svg></span></p>
  </div>
</section>

<section class="card card--back" aria-label="Business card back">
  <div class="wordmark">
    <span class="wordmark__name">TANDOR</span>
    <span class="wordmark__tag">Electrical &amp; Communications</span>
  </div>
</section>

</body>
</html>
```